website creation for contract embroidery company

We are a contract embroider located in Chicago, servicing coast to coast.

Looking for about 5 pages of web design. Home, Gallery, About us, Request Quote.

We also need help with the ad copy itself. I recommend to look at other "contract embroidery" websites to get a sense of what others in our industry is posting.

Industry/Entity Type

Embroidery

Coding

Coded - Design and coding required

Number of Pages Required

1 page

Colors
0356a4
fbee3e

```html
<!DOCTYPE html>
<html lang="en">
<head>
<meta charset="utf-8">
<title>Stitchline Works – Contract Embroidery</title>
<link href="https://fonts.googleapis.com/css2?family=Open+Sans:ital,wght@0,400;0,600;0,700;0,800;1,700;1,800&display=swap" rel="stylesheet">
<style>
:root{
  --brand-blue:#0356a4;
  --brand-blue-dark:#023f7a;
  --brand-yellow:#fbee3e;
  --ink:#333333;
  --muted:#6b6b6b;
  --panel:#f1f1f1;
  --line:#d9d9d9;
  --footer:#2b3640;
  --footer-deep:#1f2830;
  --gallery-bg:#3d3a33;
}
*{box-sizing:border-box;margin:0;padding:0}
html,body{width:859px;height:1200px;overflow:hidden;background:#fff}
body{font-family:"Open Sans",Arial,sans-serif;color:var(--ink);position:relative;font-size:9px;line-height:1.45}

/* Header */
.site-header{position:absolute;left:0;top:0;width:859px;height:86px;background:#fff}
.brand{position:absolute;left:40px;top:14px;display:flex;align-items:center;gap:8px}
.brand-mark{width:14px;height:14px;border-radius:50%;background:var(--brand-yellow)}
.brand-name{font-weight:800;font-size:24px;color:var(--brand-blue);line-height:1}
.call{position:absolute;right:40px;top:6px;display:flex;align-items:center;gap:8px}
.call-icon{width:26px;height:26px;border-radius:50%;background:var(--brand-blue);display:flex;align-items:center;justify-content:center}
.call-label{font-size:8px;font-weight:700;color:var(--muted);letter-spacing:.5px}
.call-number{font-size:15px;font-weight:800;color:var(--brand-blue);line-height:1.1}
.main-nav{position:absolute;left:330px;top:44px;width:500px;height:42px;background:var(--brand-blue);display:flex}
.main-nav a{flex:1;display:flex;align-items:center;justify-content:center;color:#fff;font-weight:700;font-size:11px;text-decoration:none}
.main-nav a.is-active{background:var(--brand-yellow);color:var(--brand-blue)}

/* Hero */
.hero{position:absolute;left:0;top:86px;width:859px;height:300px;overflow:hidden}
.hero-photo{position:absolute;inset:0;background:linear-gradient(180deg,#4d5a6a 0%,#8b8f94 45%,#b6b0a6 100%)}
.hero-panel{position:absolute;right:0;top:0;width:560px;height:300px}
.hero-copy{position:absolute;right:45px;top:66px;width:320px;text-align:right}
.hero-title{font-style:italic;font-weight:800;font-size:21px;line-height:1.22;color:var(--brand-blue)}
.btn-quote{position:absolute;right:165px;top:182px;background:var(--brand-blue);color:#fff;font-weight:700;font-size:11px;padding:9px 20px;border-radius:16px}
.hero-dots{position:absolute;left:410px;bottom:12px;display:flex;gap:6px}
.hero-dots span{width:8px;height:8px;border-radius:50%;background:#fff;opacity:.6}
.hero-dots span.is-current{opacity:1;background:var(--brand-blue)}

/* Services */
.services{position:absolute;left:0;top:386px;width:859px;height:218px;background:var(--panel);border-bottom:1px solid var(--line)}
.service-list{position:absolute;left:40px;top:22px;width:780px;display:flex;justify-content:space-between}
.service{width:176px;text-align:center}
.service-photo{width:80px;height:80px;border-radius:50%;margin:0 auto 10px;border:3px solid #fff;box-shadow:0 0 0 1px var(--line)}
.service h3{font-size:11px;font-weight:700;color:#222;line-height:1.25;margin-bottom:6px}
.service p{color:var(--muted);font-size:8.5px}
.read-more{display:inline-block;margin-top:6px;font-size:8px;font-weight:700;color:var(--brand-blue)}

/* Welcome + contact */
.intro{position:absolute;left:40px;top:622px;width:780px;height:232px;display:flex;gap:30px}
.welcome{width:452px}
.section-title{font-size:17px;font-weight:700;color:#222;margin-bottom:10px}
.section-title em{font-style:normal;color:var(--brand-blue)}
.welcome p{color:var(--muted);font-size:9px;margin-bottom:8px}
.touch{width:298px}
.touch-form{display:flex;flex-direction:column;gap:7px}
.field{height:20px;border:1px solid var(--line);padding:3px 6px;font-size:8px;color:var(--muted);background:#fff}
.field.is-message{height:52px}
.btn-submit{align-self:flex-end;background:var(--brand-blue);color:#fff;font-weight:700;font-size:9px;padding:5px 14px}

/* Gallery */
.gallery{position:absolute;left:0;top:858px;width:859px;height:157px;background:var(--gallery-bg);overflow:hidden}
.gallery-backdrop{position:absolute;inset:0;background:linear-gradient(180deg,#6a6253 0%,#3b372f 100%)}
.gallery-title{position:absolute;left:14px;top:8px;font-size:15px;font-weight:700;color:#fff}
.gallery-track{position:absolute;left:100px;top:42px;width:660px;display:flex;gap:10px}
.thumb{position:relative;flex:1;height:100px;border:3px solid #fff}
.thumb-label{position:absolute;left:0;right:0;top:36px;text-align:center;color:#fff;font-weight:700;font-size:10px}
.gallery-arrow{position:absolute;top:80px;width:20px;height:26px;background:rgba(255,255,255,.25);display:flex;align-items:center;justify-content:center}
.gallery-arrow.prev{left:62px}
.gallery-arrow.next{right:62px}

/* Footer */
.site-footer{position:absolute;left:0;top:1015px;width:859px;height:160px;background:var(--footer);color:#d5dbe0}
.footer-cols{position:absolute;left:40px;top:14px;width:780px;display:flex;gap:24px}
.footer-col h4{font-size:10.5px;font-weight:700;color:#fff;margin-bottom:8px}
.col-links{width:140px}
.col-contact{width:210px}
.col-map{width:220px}
.col-follow{width:140px}
.footer-list{list-style:none}
.footer-list li{font-size:8.5px;margin-bottom:4px;display:flex;align-items:center;gap:6px}
.bullet{width:4px;height:4px;background:var(--brand-yellow)}
.contact-row{display:flex;gap:7px;font-size:8.5px;margin-bottom:7px;align-items:flex-start}
.map-area{width:200px;height:92px;border:2px solid #fff}
.social-dot{width:14px;height:14px;border-radius:50%;background:var(--brand-blue)}
.copyright{position:absolute;left:0;bottom:0;width:859px;height:25px;background:var(--footer-deep);color:#a7b0b8;font-size:8px;display:flex;align-items:center;justify-content:center}
</style>
</head>
<body>

<header class="site-header">
  <div class="brand"><span class="brand-mark"></span><span class="brand-name">Stitchline Works</span></div>
  <div class="call">
    <span class="call-icon">
      <svg width="14" height="14" viewBox="0 0 24 24"><path fill="#fff" d="M6.6 10.8c1.4 2.8 3.8 5.1 6.6 6.6l2.2-2.2c.3-.3.7-.4 1-.2 1.1.4 2.3.6 3.6.6.6 0 1 .4 1 1V20c0 .6-.4 1-1 1C10.6 21 3 13.4 3 4c0-.6.4-1 1-1h3.5c.6 0 1 .4 1 1 0 1.3.2 2.5.6 3.6.1.3 0 .7-.2 1l-2.3 2.2z"/></svg>
    </span>
    <div>
      <div class="call-label">CALL US TODAY</div>
      <div class="call-number">555-013-2468</div>
    </div>
  </div>
  <nav class="main-nav">
    <a class="is-active">HOME</a><a>GALLERY</a><a>SERVICES</a><a>ABOUT US</a><a>REQUEST QUOTE</a>
  </nav>
</header>

<section class="hero">
  <div class="hero-photo" role="img" aria-label="Photo of a row of multi-head embroidery machines on a production floor"></div>
  <svg class="hero-panel" width="560" height="300" viewBox="0 0 560 300" aria-hidden="true">
    <path d="M90 0 C10 80 20 220 120 300 L560 300 L560 0 Z" fill="#ffffff" opacity=".95"/>
    <path d="M90 0 C10 80 20 220 120 300" fill="none" stroke="#0356a4" stroke-width="4"/>
  </svg>
  <div class="hero-copy">
    <p class="hero-title">We are a contract embroiders located in Chicago and servicing coast to coast.</p>
  </div>
  <span class="btn-quote">FREE QUOTE</span>
  <div class="hero-dots"><span class="is-current"></span><span></span><span></span><span></span></div>
</section>

<section class="services">
  <div class="service-list">
    <article class="service">
      <div class="service-photo" role="img" aria-label="Photo of custom embroidered shirts" style="background:linear-gradient(135deg,#2f4a6d,#8a97a8)"></div>
      <h3>Custom Embroidered<br>Clothing</h3>
      <p>Sharp, durable stitching on shirts, jackets and caps for any team.</p>
      <span class="read-more">READ MORE ›</span>
    </article>
    <article class="service">
      <div class="service-photo" role="img" aria-label="Photo of embroidered golf clothing" style="background:linear-gradient(135deg,#b9c4cf,#e8e8e8)"></div>
      <h3>Embroidered Golf<br>Clothes</h3>
      <p>Polos, pullovers and hats finished cleanly for clubs and tournaments.</p>
      <span class="read-more">READ MORE ›</span>
    </article>
    <article class="service">
      <div class="service-photo" role="img" aria-label="Photo of garment labels" style="background:linear-gradient(135deg,#c9c2b4,#f2efe8)"></div>
      <h3>Re-Labeling</h3>
      <p>Fast label swaps and neck tags done to your exact specs.</p>
      <span class="read-more">READ MORE ›</span>
    </article>
    <article class="service">
      <div class="service-photo" role="img" aria-label="Photo of an embroidery machine stitching a design" style="background:linear-gradient(135deg,#6d6f73,#c4c1bb)"></div>
      <h3>Digitizing</h3>
      <p>Artwork converted into clean stitch files ready for any machine.</p>
      <span class="read-more">READ MORE ›</span>
    </article>
  </div>
</section>

<section class="intro">
  <div class="welcome">
    <h2 class="section-title">Welcome To <em>Stitchline Works</em></h2>
    <p>We run a full floor of multi-head machines in Chicago and ship finished orders to clients from coast to coast. Our crew handles short runs and large volume jobs with the same care, checking every piece for thread tension, placement and color before it leaves the shop. Bring us your logo, your blanks and your deadline, and we will turn it around on time.</p>
    <p>Ask about rush service, private labeling and wholesale pricing for repeat accounts.</p>
  </div>
  <div class="touch">
    <h2 class="section-title">Get In <em>Touch With Us</em></h2>
    <form class="touch-form">
      <div class="field">Your Name</div>
      <div class="field">Phone</div>
      <div class="field">Email</div>
      <div class="field is-message">Message</div>
      <span class="btn-submit">SUBMIT</span>
    </form>
  </div>
</section>

<section class="gallery">
  <div class="gallery-backdrop" role="img" aria-label="Dimmed background photo of thread spools on a workshop wall"></div>
  <h2 class="gallery-title">Projects Gallery</h2>
  <span class="gallery-arrow prev"><svg width="8" height="12" viewBox="0 0 8 12"><path d="M7 1 2 6l5 5" fill="none" stroke="#fff" stroke-width="2"/></svg></span>
  <div class="gallery-track">
    <div class="thumb" role="img" aria-label="Photo of embroidery machines in operation" style="background:linear-gradient(135deg,#5c6470,#a9a59b)"></div>
    <div class="thumb" role="img" aria-label="Photo of finished embroidered jackets" style="background:linear-gradient(135deg,#2a5590,#6f8fb8)"><span class="thumb-label">Team Jackets</span></div>
    <div class="thumb" role="img" aria-label="Photo of stitched patches" style="background:linear-gradient(135deg,#7a7060,#c9bfa9)"></div>
    <div class="thumb" role="img" aria-label="Photo of embroidered caps" style="background:linear-gradient(135deg,#4e4a44,#9b9489)"></div>
  </div>
  <span class="gallery-arrow next"><svg width="8" height="12" viewBox="0 0 8 12"><path d="M1 1l5 5-5 5" fill="none" stroke="#fff" stroke-width="2"/></svg></span>
</section>

<footer class="site-footer">
  <div class="footer-cols">
    <div class="footer-col col-links">
      <h4>Quick Links</h4>
      <ul class="footer-list">
        <li><span class="bullet"></span>Home</li>
        <li><span class="bullet"></span>Gallery</li>
        <li><span class="bullet"></span>Services</li>
        <li><span class="bullet"></span>About Us</li>
        <li><span class="bullet"></span>Request Quote</li>
      </ul>
    </div>
    <div class="footer-col col-contact">
      <h4>Contact Information</h4>
      <div class="contact-row">
        <svg width="10" height="12" viewBox="0 0 10 14"><path d="M5 0C2.2 0 0 2.2 0 5c0 3.6 5 9 5 9s5-5.4 5-9c0-2.8-2.2-5-5-5zm0 7a2 2 0 1 1 0-4 2 2 0 0 1 0 4z" fill="#fbee3e"/></svg>
        <span>1200 Loom Street, Suite 4, Chicago, IL 60607</span>
      </div>
      <div class="contact-row">
        <svg width="10" height="10" viewBox="0 0 24 24"><path fill="#fbee3e" d="M6.6 10.8c1.4 2.8 3.8 5.1 6.6 6.6l2.2-2.2c.3-.3.7-.4 1-.2 1.1.4 2.3.6 3.6.6.6 0 1 .4 1 1V20c0 .6-.4 1-1 1C10.6 21 3 13.4 3 4c0-.6.4-1 1-1h3.5c.6 0 1 .4 1 1 0 1.3.2 2.5.6 3.6.1.3 0 .7-.2 1l-2.3 2.2z"/></svg>
        <span>555-013-2468</span>
      </div>
      <div class="contact-row">
        <svg width="11" height="9" viewBox="0 0 12 9"><rect x=".5" y=".5" width="11" height="8" fill="none" stroke="#fbee3e"/><path d="M.5.5 6 5l5.5-4.5" fill="none" stroke="#fbee3e"/></svg>
        <span>hello@stitchlineworks.com</span>
      </div>
    </div>
    <div class="footer-col col-map">
      <h4>Location Map</h4>
      <div class="map-area" role="img" aria-label="Street map showing the shop location in Chicago" style="background:linear-gradient(135deg,#e7e3d8,#cfd8c4)"></div>
    </div>
    <div class="footer-col col-follow">
      <h4>Follow Us</h4>
      <ul class="footer-list">
        <li><span class="social-dot"></span>Feedpage</li>
        <li><span class="social-dot"></span>Chirper</li>
        <li><span class="social-dot"></span>Circleplus</li>
        <li><span class="social-dot"></span>Worknet</li>
      </ul>
    </div>
  </div>
  <div class="copyright">© 2015 Stitchline Works &nbsp;|&nbsp; All rights reserved</div>
</footer>

</body>
</html>
```